Real Estate "For Sale" Sign for construction company

We need a sign that we can use to hang on a post and place on the road when we sell a property. The sign will be simple and will need to mainly feature our logo (files attached), as well as the words "For Sale", and then our phone number "(555) 617 3489". The sign will hang on a post that'll look something like the attached picture.

Target Market(s)

Home buyers

Industry/Entity Type

Real Estate

Font styles to use
Serif
Sans Serif

Colors
0054AA
0677BA
7BADD7
CADEEF
E8F1F8
0094D4
00A9DD
6FCCEA
C7EBF8
E9F6FB

Requirements
Must have
• For Sale & our phone number

```html
<!DOCTYPE html>
<html lang="en">
<head>
<meta charset="utf-8">
<title>For Sale Sign – Northern Ridge Properties</title>
<link rel="stylesheet" href="https://fonts.googleapis.com/css2?family=EB+Garamond:wght@500;600&family=Montserrat:wght@500&display=swap">
<style>
  :root {
    --backdrop: #b8b8b8;
    --navy: #121f4b;
    --sky: #8fd8f8;
    --rule: #8ed8f8;
    --white: #ffffff;
  }
  html, body {
    margin: 0;
    padding: 0;
    width: 1200px;
    height: 1200px;
    overflow: hidden;
    background: var(--backdrop);
  }
  .sign {
    position: absolute;
    left: 250px;
    top: 77px;
    width: 700px;
    height: 1046px;
    background: var(--sky);
    box-shadow: 0 4px 14px rgba(0, 0, 0, 0.35);
  }
  .sign-header {
    position: absolute;
    left: 0;
    top: 0;
    width: 100%;
    height: 409px;
    background: var(--navy);
    color: var(--white);
    font-family: "EB Garamond", Georgia, serif;
    text-align: center;
  }
  .headline {
    position: absolute;
    left: 0;
    right: 0;
    top: 56px;
    margin: 0;
    font-weight: 600;
    font-size: 130px;
    line-height: 1;
    letter-spacing: 6px;
    padding-left: 6px;
  }
  .headline .small-cap {
    font-size: 98px;
  }
  .divider {
    position: absolute;
    left: 106px;
    top: 223px;
    width: 481px;
    height: 6px;
    background: var(--rule);
  }
  .phone {
    position: absolute;
    left: 0;
    right: 0;
    top: 280px;
    margin: 0;
    font-weight: 500;
    font-size: 76px;
    line-height: 1;
    letter-spacing: 1px;
    font-variant-numeric: lining-nums;
  }
  .brand {
    position: absolute;
    left: 0;
    right: 0;
    top: 0;
    bottom: 0;
    text-align: center;
    color: var(--navy);
    font-family: "Montserrat", Arial, sans-serif;
    font-weight: 500;
  }
  .brand-mark {
    position: absolute;
    left: 130px;
    top: 478px;
    width: 440px;
    height: 440px;
    border-radius: 50%;
    background: var(--navy);
  }
  .brand-name {
    position: absolute;
    left: 0;
    right: 0;
    top: 922px;
    margin: 0;
    font-size: 52px;
    line-height: 1;
    letter-spacing: 0.5px;
  }
  .brand-tagline {
    position: absolute;
    left: 0;
    right: 0;
    top: 1010px;
    margin: 0;
    font-size: 13px;
    line-height: 1;
    letter-spacing: 17px;
    padding-left: 17px;
  }
</style>
</head>
<body>
  <main class="sign">
    <header class="sign-header">
      <h1 class="headline">F<span class="small-cap">OR</span> S<span class="small-cap">ALE</span></h1>
      <div class="divider"></div>
      <p class="phone">(555) 617 3489</p>
    </header>
    <section class="brand">
      <span class="brand-mark" aria-hidden="true"></span>
      <p class="brand-name">Northern Ridge</p>
      <p class="brand-tagline">PROPERTIES</p>
    </section>
  </main>
</body>
</html>
```